I would love for my business card to be fun and sophisicated. The clients are people that could afford nice well crafted wigs. These wigs are not like granny wigs. The're for women who are stylish and what to look there best especially if they are dealing with cancer are some from of hair loss. Do not want the card to appear crowded with to much information. If I need to eliminate some data, let me know.
Thanks

Industry/Entity Type

Hair

Contact Information for Business Card

L Radiant Tresses, Marianne Holt, owner, stylist

Wigs/Studio Showroom
Extensions
Hair Replacement
Private Room

24618 Crest Meadow Loop, Suite. R
Irvine, CA 90377
(949) 582-7041
Email: wigs@lradianttresses-example.com
www.lradianttresses-example.com

```html
<!DOCTYPE html>
<html lang="en">
<head>
<meta charset="utf-8">
<title>L Radiant Tresses – Business Card</title>
<link rel="stylesheet" href="https://fonts.googleapis.com/css2?family=Didact+Gothic&family=Poiret+One&family=Comfortaa:wght@400&display=swap">
<style>
  :root {
    --card-navy: #14094c;
    --brand-red: #e42329;
    --name-green: #a9d59f;
    --contact-blue: #b3e2ee;
    --swirl-tone: #2c2a6b;
    --hair-magenta: #e5087f;
    --skin-teal: #70c9d2;
    --hair-pink: #f2909c;
    --white: #ffffff;
  }
  * { margin: 0; padding: 0; box-sizing: border-box; }
  html, body {
    width: 1200px;
    height: 702px;
    overflow: hidden;
    background: var(--card-navy);
  }
  .card {
    position: relative;
    width: 1200px;
    height: 702px;
    background: var(--card-navy);
    overflow: hidden;
  }
  .swirl-decor {
    position: absolute;
    left: 0;
    top: 250px;
    width: 700px;
    height: 452px;
  }
  .portrait-art {
    position: absolute;
    left: 580px;
    top: 0;
    width: 620px;
    height: 702px;
  }
  .brand-name {
    position: absolute;
    left: 88px;
    top: 92px;
    width: 500px;
    font-family: "Didact Gothic", sans-serif;
    font-weight: 400;
    font-size: 70px;
    line-height: 1.05;
    color: var(--brand-red);
  }
  .person {
    position: absolute;
    left: 96px;
    top: 330px;
    width: 470px;
    text-align: center;
  }
  .person-name {
    font-family: "Didact Gothic", sans-serif;
    font-size: 40px;
    letter-spacing: 0.5px;
    color: var(--name-green);
    text-transform: uppercase;
  }
  .person-role {
    margin-top: 12px;
    font-family: "Poiret One", sans-serif;
    font-size: 34px;
    color: var(--name-green);
  }
  .address {
    position: absolute;
    left: 96px;
    top: 520px;
    width: 470px;
    text-align: center;
    font-family: "Comfortaa", sans-serif;
    font-size: 22px;
    line-height: 40px;
    color: var(--contact-blue);
    font-style: normal;
  }
  .web-line {
    position: absolute;
    left: 28px;
    top: 650px;
    font-family: "Comfortaa", sans-serif;
    font-size: 19px;
    color: var(--contact-blue);
  }
  .web-line.site { left: 390px; }
  .services {
    position: absolute;
    left: 1160px;
    top: 672px;
    transform: rotate(-90deg);
    transform-origin: 0 0;
    white-space: nowrap;
    font-family: "Poiret One", sans-serif;
    font-size: 23px;
    letter-spacing: 1.5px;
    color: var(--white);
  }
</style>
</head>
<body>
  <main class="card">
    <svg class="swirl-decor" role="img" aria-label="Faint decorative swirl pattern" viewBox="0 0 700 452">
      <defs>
        <radialGradient id="swirlGlow" cx="40%" cy="65%" r="60%">
          <stop offset="0%" stop-color="#2c2a6b" stop-opacity="0.75"/>
          <stop offset="100%" stop-color="#2c2a6b" stop-opacity="0"/>
        </radialGradient>
      </defs>
      <rect width="700" height="452" fill="url(#swirlGlow)"/>
    </svg>

    <svg class="portrait-art" role="img" aria-label="Illustration of a woman's profile with long flowing pink and magenta hair" viewBox="0 0 620 702">
      <defs>
        <linearGradient id="portraitTones" x1="0" y1="0" x2="1" y2="0">
          <stop offset="0%" stop-color="#e5087f"/>
          <stop offset="40%" stop-color="#e5087f"/>
          <stop offset="55%" stop-color="#70c9d2"/>
          <stop offset="70%" stop-color="#14094c"/>
          <stop offset="80%" stop-color="#14094c"/>
          <stop offset="88%" stop-color="#f2909c"/>
          <stop offset="92%" stop-color="#14094c"/>
          <stop offset="100%" stop-color="#14094c"/>
        </linearGradient>
      </defs>
      <path d="M317 0 C200 120 60 300 20 500 C10 570 60 640 180 702 L620 702 L620 0 Z" fill="url(#portraitTones)"/>
    </svg>

    <h1 class="brand-name">L Radiant Tresses</h1>

    <section class="person">
      <p class="person-name">Marianne Holt</p>
      <p class="person-role">Owner / Stylist</p>
    </section>

    <address class="address">
      Private Room 24618 Crest Meadow Loop,<br>
      Suite. R, Irvine, CA 90377<br>
      (949) 582-7041
    </address>

    <p class="web-line email">wigs@lradianttresses-example.com</p>
    <p class="web-line site">www.lradianttresses-example.com</p>

    <p class="services">Wigs/Studio Showroom . Extensions . Hair Replacement .</p>
  </main>
</body>
</html>
```